【 概要 】 居酒屋の新メニューデザートのPOP 【 依頼内容 】 ・サイズ: A4サイズ ・作成数: 1種類 ・素材の用意(画像・文章等):こちらで用意します ・デザイン内容:商品名、キャッチコピー、写真を載せてください。 抹茶ティラミスとイチゴティラミスの2品のPOP 両方とも枡に入っています、京都などで同じようにだしているお店を参考にしました。 【 デザインイメージ 】 ・ターゲット層:来店する20〜50代女性 ・雰囲気:ナチュラルでおしゃれな雰囲気 ・その他ご質参考デザイン: お店の雰囲気などからデザインを考えていただきたいです、 参考URLにお店のページをのせたのでご参考ください。 問等ありましたら、気軽にお問い合わせください。 ご応募をお待ちしております! |
| https://umaimappu.jp/okinawa/B5812/B581204/58136042/ | ||
どこか品があるようなそしてお店の雰囲気にも合いそうなデザインだったのでこみらを採用させていただきました。
皆さまこの度はご提案ありがとうございます。
また利用させていただくことがあると思いますので宜しくお願いします。

```html
<!DOCTYPE html>
<html lang="ja">
<head>
<meta charset="utf-8">
<title>お店でお花見しませんか? 新作ティラミス</title>
<link rel="stylesheet" href="https://fonts.googleapis.com/css2?family=Klee+One:wght@400;600&family=Yomogi&display=swap">
<style>
  :root {
    --paper: #ffffff;
    --ink: #2b2b2b;
    --frame: #1e1e1e;
    --matcha-band: #d6e5b6;
    --matcha-line: #2fa43a;
    --ichigo-band: #f3a9bb;
    --ichigo-line: #e2347a;
    --photo-wood: #d8b48f;
    --photo-light: #efe3d3;
  }
  * { margin: 0; padding: 0; box-sizing: border-box; }
  html, body { width: 848px; height: 1200px; overflow: hidden; background: var(--paper); }
  .pop {
    position: relative;
    width: 848px; height: 1200px;
    background: var(--paper);
    color: var(--ink);
    font-family: "Klee One", "Yomogi", sans-serif;
  }
  .pop__frame {
    position: absolute; left: 21px; top: 21px; right: 21px; bottom: 21px;
    border: 5px solid var(--frame);
    border-radius: 32px;
    overflow: hidden;
  }
  .headline {
    position: absolute; left: 0; right: 0; top: 138px;
    text-align: center;
    white-space: nowrap;
    font-weight: 600;
    font-size: 60px;
    letter-spacing: 1px;
    line-height: 1;
  }
  .lead {
    position: absolute; left: 0; right: 0; top: 228px;
    text-align: center;
    white-space: nowrap;
    font-family: "Yomogi", sans-serif;
    font-size: 32px;
    line-height: 1.2;
    letter-spacing: 2px;
  }
  .band { position: absolute; left: 0; right: 0; }
  .band--matcha { top: 410px; height: 300px; background: var(--matcha-band); }
  .band--ichigo { top: 783px; height: 273px; background: var(--ichigo-band); }
  .band__line { position: absolute; left: 0; right: 0; height: 8px; }
  .band--matcha .band__line { top: 232px; background: var(--matcha-line); }
  .band--ichigo .band__line { top: 220px; background: var(--ichigo-line); }
  .band__mark { position: absolute; width: 56px; height: 56px; border-radius: 50%; }
  .band--matcha .band__mark { left: 715px; top: 208px; background: var(--matcha-line); }
  .band--ichigo .band__mark { left: 32px; top: 196px; background: var(--ichigo-line); }
  .photo { position: absolute; }
  .photo--matcha {
    left: 45px; top: 0; width: 437px; height: 300px;
    background: radial-gradient(ellipse at 50% 45%, #8da45a 0 18%, var(--photo-wood) 30%, var(--photo-light) 80%);
  }
  .photo--ichigo {
    left: 324px; top: 0; width: 405px; height: 268px;
    background: radial-gradient(ellipse at 50% 45%, #d96b8c 0 18%, var(--photo-wood) 30%, var(--photo-light) 80%);
  }
  .label {
    position: absolute;
    white-space: nowrap;
    font-family: "Yomogi", sans-serif;
    font-size: 30px;
    line-height: 1.2;
    letter-spacing: 2px;
  }
  .label--matcha { left: 45px; top: 726px; }
  .label--ichigo { right: 30px; top: 1076px; }
</style>
</head>
<body>
  <main class="pop">
    <div class="pop__frame">
      <h1 class="headline">お店でお花見しませんか?</h1>
      <p class="lead">浜かぜが手がける新作スイーツの登場です。</p>

      <section class="band band--matcha">
        <div class="band__line"></div>
        <div class="band__mark" role="img" aria-label="緑の花のマーク"></div>
        <div class="photo photo--matcha" role="img" aria-label="枡に入った抹茶ティラミスと木のスプーンの写真"></div>
      </section>
      <p class="label label--matcha">抹茶ティラミス</p>

      <section class="band band--ichigo">
        <div class="band__line"></div>
        <div class="band__mark" role="img" aria-label="ピンクの花のマーク"></div>
        <div class="photo photo--ichigo" role="img" aria-label="枡に入ったいちごティラミスと木のスプーンの写真"></div>
      </section>
      <p class="label label--ichigo">いちごティラミス</p>
    </div>
  </main>
</body>
</html>
```